Vantro #27 - MEN'S NATURAL THERAPEUTIC INTIMATE WASH

Men's Natural Therapeutic INTIMATE Wash
VANTRO #27

Design a 4 oz. stand up tube with flip top cap...
To be packaged in a carton/box

Formula contains Tea Tree OIL
Aloe Vera Gel
Coconut Oil

PRODUCT IS A WASH/SOAP

Helps with
- Jock Itch (tinea cruris)
- Skin Rashes
- Candida
- Itchy Skin

COLORS ON TUBE: Gray, Black, Lime Electric Green and Blue

PRODUCT FOR MEN!

Target Market(s)

MEN

Industry/Entity Type

Retail

Font styles to use
Sans Serif

Colors
9bcb3b
abd036
33a6d7
000000
c9c9c9

Requirements
Must have
• Colors... black, gray, electric green and blue
Nice to have
• Needs to look masculine appeal to the male consumer

```html
<!DOCTYPE html>
<html lang="en">
<head>
<meta charset="utf-8">
<title>Vantro #27 – Men's Natural Therapeutic Intimate Wash</title>
<link rel="stylesheet" href="https://fonts.googleapis.com/css2?family=Exo+2:ital,wght@1,500;1,700&family=Montserrat:wght@700;800&family=Questrial&display=swap">
<style>
  :root {
    --black: #000000;
    --lime: #abd036;
    --lime-deep: #9bcb3b;
    --blue: #33a6d7;
    --gray: #c9c9c9;
    --gray-dark: #8c8c8c;
    --white: #ffffff;
    --backdrop: #f2f2f2;
    --ink: #1b1b1b;
  }
  * { margin: 0; padding: 0; box-sizing: border-box; }
  html, body { width: 1200px; height: 1185px; overflow: hidden; background: var(--backdrop); }
  .canvas { position: relative; width: 1200px; height: 1185px; }

  .label {
    position: absolute; left: 320px; top: 130px; width: 560px; height: 900px;
    background: var(--black); overflow: hidden;
  }
  .crimp {
    position: absolute; left: 0; top: 0; width: 100%; height: 50px;
    background: repeating-linear-gradient(90deg, #3a3a3a 0 4px, var(--black) 4px 9px);
    border-bottom: 6px solid var(--black);
  }
  .pattern-strip {
    position: absolute; right: 14px; top: 130px; width: 90px; height: 640px;
    background: linear-gradient(180deg, var(--lime) 0%, var(--lime-deep) 100%);
    opacity: .9;
  }
  .pattern-band {
    position: absolute; left: 0; bottom: 0; width: 100%; height: 104px;
    background: linear-gradient(90deg, var(--gray) 0%, var(--gray) 50%, var(--lime) 75%, var(--gray) 100%);
  }

  .ingredients {
    position: absolute; left: 150px; top: 110px;
    font-family: 'Exo 2', sans-serif; font-style: italic; font-weight: 700;
    font-variant: small-caps; color: var(--lime); font-size: 27px; line-height: 31px;
  }
  .ingredients span { display: block; }
  .ingredients .i2 { padding-left: 60px; }
  .ingredients .i3 { padding-left: 50px; }

  .descriptor {
    position: absolute; left: 140px; top: 265px; color: var(--white);
    font-family: 'Questrial', sans-serif; font-weight: 400; line-height: 1;
  }
  .descriptor .d1 { display: block; font-size: 27px; }
  .descriptor .d2 { display: block; font-size: 37px; margin-top: 3px; }

  .product-name {
    position: absolute; left: 150px; top: 375px; color: var(--lime);
    font-family: 'Montserrat', sans-serif; font-weight: 800; line-height: 1;
  }
  .product-name .n1 { display: block; font-size: 50px; letter-spacing: 2px; }
  .product-name .n2 { display: block; font-size: 140px; margin-top: 8px; letter-spacing: -4px; }

  .audience {
    position: absolute; left: 176px; top: 640px; width: 220px; height: 46px;
    border: 4px solid var(--gray-dark); border-radius: 14px;
    background: linear-gradient(180deg, #7cc6ea 0%, var(--blue) 100%);
    font-family: 'Montserrat', sans-serif; font-weight: 800; font-size: 27px;
    color: var(--ink); text-align: center; line-height: 38px; letter-spacing: 1px;
  }

  .helps-tag {
    position: absolute; left: 96px; top: 730px; width: 30px; height: 110px;
    background: var(--gray); border: 2px solid var(--white); border-radius: 8px;
    writing-mode: vertical-rl; transform: rotate(180deg);
    font-family: 'Montserrat', sans-serif; font-weight: 800; font-size: 12px;
    color: var(--ink); text-align: center; line-height: 26px;
  }
  .benefits {
    position: absolute; left: 138px; top: 722px; list-style: none;
    font-family: 'Exo 2', sans-serif; font-style: italic; font-weight: 500;
    font-size: 31px; line-height: 36px;
  }
  .benefits .on-dark { color: var(--lime); }
  .benefits .on-light { color: var(--ink); }
</style>
</head>
<body>
<main class="canvas">
  <section class="label">
    <div class="crimp"></div>
    <div class="pattern-strip" role="img" aria-label="Lime green checkered square pattern running down the right edge"></div>
    <div class="pattern-band" role="img" aria-label="Gray and lime green checkered square pattern along the bottom"></div>

    <p class="ingredients">
      <span class="i1">With Tea Tree Oil</span>
      <span class="i2">Aloe Vera Gel</span>
      <span class="i3">Coconut Oil</span>
    </p>

    <h2 class="descriptor">
      <span class="d1">Natural Therapeutic</span>
      <span class="d2">INTIMATE Wash</span>
    </h2>

    <h1 class="product-name">
      <span class="n1">VANTRO</span>
      <span class="n2">#27</span>
    </h1>

    <div class="audience">FOR MAN</div>

    <div class="helps-tag">HELPS WITH</div>
    <ul class="benefits">
      <li class="on-dark">Jock Itch</li>
      <li class="on-dark">Skin Rashes</li>
      <li class="on-light">Candida</li>
      <li class="on-light">Itchy Skin</li>
    </ul>
  </section>
</main>
</body>
</html>
```